Bed Company needs business card

Hello, we are a bed company that makes specialized magnets for beds. We are an alternative healing company. I need a modern and upscale business card. Please incorporate my logo for the card.

Accepted file formats are AI, EPS, and Press-Ready PDFS.

Please include all fonts or convert them to outlines regardless of file type.

If you are designing the card in Photoshop the file Must be 1200dpi.

I am open to anything for the business card.  I really like all of your designs and if you want to change the color of the logo, you can.  I will be making the final selection by Friday.  Thank You for all of your designs.  Feel Free to submit different color logos if you want.  

Reason: I will make a decision Final on Friday April 20th. 2012. Good Luck and Thank you all for the designs.

Target Market(s)

My target Market is people, who are looking for alternative healing.

Industry/Entity Type

Business

Requirements
Must have
• My logo must be incorporated. The front card must have

Name
Job Title

Address
Work
Cell
Fax
email
web

Just put in fake info for the card.

The back of the card. I want the logo on the back with color. I just want it to look modern and cool.

```html
<!DOCTYPE html>
<html lang="en">
<head>
<meta charset="utf-8">
<title>Lodestone Rest – Business Card</title>
<link rel="stylesheet" href="https://fonts.googleapis.com/css2?family=Open+Sans:wght@400;600&display=swap">
<style>
  :root {
    --band-green: #6aae45;
    --deep-green: #1f6a2c;
    --ink: #3a3a3a;
    --paper: #ffffff;
    --backdrop: #e9e7e4;
  }
  * { margin: 0; padding: 0; box-sizing: border-box; }
  html, body {
    width: 1200px; height: 900px; overflow: hidden;
    background: var(--backdrop);
    font-family: "Open Sans", Arial, sans-serif;
  }
  .card {
    position: absolute;
    width: 560px; height: 320px;
    background: var(--paper);
    box-shadow: 0 3px 10px rgba(0,0,0,0.18);
    overflow: hidden;
  }
  .card-front { left: 80px; top: 110px; }
  .card-back { left: 560px; top: 470px; }

  .band { position: absolute; left: 0; width: 100%; background: var(--band-green); }
  .card-front .band-top { top: 0; height: 30px; }
  .card-front .band-bottom {
    bottom: 0; height: 40px;
    color: var(--paper); font-size: 10.5px;
    display: flex; align-items: center; justify-content: center;
  }
  .card-back .band-top { top: 0; height: 26px; }
  .card-back .band-bottom {
    bottom: 0; height: 54px;
    color: var(--paper); font-size: 14px; font-weight: 600;
    display: flex; align-items: center; justify-content: center;
    letter-spacing: 0.3px;
  }

  .identity { position: absolute; top: 68px; left: 0; width: 100%; text-align: center; }
  .person-name { font-size: 31px; font-weight: 400; color: var(--ink); line-height: 1.1; }
  .job-title { font-size: 17px; color: var(--deep-green); margin-top: 2px; }

  .contacts {
    position: absolute; left: 208px; top: 150px;
    font-size: 13.5px; color: var(--ink); line-height: 19px;
  }
  .contact-row { display: flex; }
  .contact-label { width: 38px; }
  .contact-sep { width: 20px; }
  .contact-email { margin-top: 22px; }

  .brand {
    position: absolute; left: 0; top: 118px; width: 100%;
    display: flex; align-items: center; justify-content: center; gap: 12px;
  }
  .brand-mark { width: 30px; height: 30px; background: var(--deep-green); }
  .brand-name { font-size: 30px; font-weight: 600; color: var(--band-green); }
</style>
</head>
<body>
  <section class="card card-front">
    <div class="band band-top"></div>
    <div class="identity">
      <h1 class="person-name">Daniel Hart</h1>
      <p class="job-title">director</p>
    </div>
    <div class="contacts">
      <div class="contact-row"><span class="contact-label">tel</span><span class="contact-sep">:</span><span>(999) 999 999</span></div>
      <div class="contact-row"><span class="contact-label">cell</span><span class="contact-sep">:</span><span>(999) 999 000</span></div>
      <div class="contact-row"><span class="contact-label">fax</span><span class="contact-sep">:</span><span>(999) 000 000</span></div>
      <div class="contact-email">office@lodestonerest.com</div>
    </div>
    <div class="band band-bottom">May 14-17, 2012, Harbor Hall West, Lakeside IL, Booth 2286</div>
  </section>

  <section class="card card-back">
    <div class="band band-top"></div>
    <div class="brand">
      <span class="brand-mark"></span>
      <span class="brand-name">Lodestone Rest</span>
    </div>
    <div class="band band-bottom">www.lodestone-rest.com</div>
  </section>
</body>
</html>
```